Billboard for Law Firm

I am looking for a billboard designs. Our branding right now is not good. The logo has to stay the same, but please help come up with something modern, airy, perhaps geometric for the supporting design elements.
Colors should probably be red and blue, or shades of blue, but you can play with the exact shades. Doesn't have to match what you see in the attachment.

The billboard should include:

- Some type of design to bring it to life.

- Logo

- Accident & Injury Law

- 614.300.7000

- Disclaimer (very small text): No Representation Made That The Quality of Legal Services Performed is Greater Than the Those of Other Attorneys

Slogan (very large): Grits, Gravy, and a Good Attorney

______________

Target Market(s)

Southern United States

Industry/Entity Type

Legal Services

Font styles to use
Serif
Sans Serif

Colors
0054AA
0677BA
7BADD7
CADEEF
E8F1F8
EB3D1F
EC4F4E
F09395
F8D3D4
FCEDEE

Requirements
Must have
• Help Make it Memorable and Easy to Read (large text for slogan)
Nice to have
• Some shapes or design elements that may become part of our branding.

```html
<!DOCTYPE html>
<html lang="en">
<head>
<meta charset="utf-8">
<title>Harlow Firm Billboard</title>
<link href="https://fonts.googleapis.com/css2?family=Bebas+Neue&family=Montserrat:wght@800&family=Poppins:wght@600;700&display=swap" rel="stylesheet">
<style>
  :root {
    --navy: #0b0c3c;
    --navy-deep: #07082b;
    --red: #d52b28;
    --white: #ffffff;
    --page: #e6e8ec;
    --photo-dark: #2a1c1a;
    --photo-warm: #8a4a30;
  }
  html, body {
    margin: 0;
    width: 903px;
    height: 1200px;
    overflow: hidden;
    background: var(--page);
  }
  .billboard {
    position: absolute;
    left: 20px;
    top: 414px;
    width: 863px;
    height: 371px;
    box-shadow: 0 14px 30px rgba(0,0,0,0.35);
  }
  .billboard svg { display: block; }
  .headline-white { font-family: "Poppins", sans-serif; font-weight: 700; fill: var(--white); }
  .headline-red { font-family: "Bebas Neue", sans-serif; fill: var(--red); }
  .practice-area { font-family: "Montserrat", sans-serif; font-weight: 800; fill: var(--navy-deep); }
  .firm-name { font-family: "Poppins", sans-serif; font-weight: 600; fill: var(--white); }
  .phone-number { font-family: "Bebas Neue", sans-serif; fill: var(--white); }
  .disclaimer { font-family: "Poppins", sans-serif; font-weight: 600; fill: var(--white); font-size: 12.5px; }
</style>
</head>
<body>
<div class="billboard">
  <svg width="863" height="371" viewBox="0 0 863 371" xmlns="http://www.w3.org/2000/svg">
    <defs>
      <linearGradient id="bg-gradient" x1="0" y1="0" x2="1" y2="1">
        <stop offset="0" stop-color="#0d0e44"/>
        <stop offset="1" stop-color="#07082b"/>
      </linearGradient>
      <linearGradient id="photo-gradient" x1="0" y1="0" x2="1" y2="1">
        <stop offset="0" stop-color="#3a2522"/>
        <stop offset="0.5" stop-color="#6b3826"/>
        <stop offset="1" stop-color="#9a6240"/>
      </linearGradient>
    </defs>

    <!-- background -->
    <rect class="board-bg" width="863" height="371" fill="url(#bg-gradient)"/>

    <!-- corner accents -->
    <g class="corner-accent">
      <rect x="717" y="0" width="7" height="34" fill="var(--red)"/>
      <rect x="728" y="0" width="7" height="34" fill="var(--red)"/>
      <rect x="739" y="0" width="7" height="34" fill="var(--red)"/>
      <rect x="746" y="0" width="117" height="34" fill="var(--white)"/>
      <rect x="717" y="338" width="7" height="33" fill="var(--red)"/>
      <rect x="728" y="338" width="7" height="33" fill="var(--red)"/>
      <rect x="739" y="338" width="7" height="33" fill="var(--red)"/>
      <rect x="746" y="338" width="117" height="33" fill="var(--white)"/>
    </g>

    <!-- photo frame -->
    <rect class="photo-frame" x="599" y="34" width="264" height="304" fill="var(--white)"/>
    <rect class="photo" x="605" y="40" width="258" height="292" fill="url(#photo-gradient)"
          role="img" aria-label="Brass scales of justice on a wooden courtroom table in warm light"/>

    <!-- slogan -->
    <text class="headline-white" x="32" y="84" font-size="48" textLength="511" lengthAdjust="spacingAndGlyphs">GRITS, GRAVY, AND</text>
    <text class="headline-red" x="32" y="164" font-size="99" textLength="539" lengthAdjust="spacingAndGlyphs">A GOOD ATTORNEY</text>

    <!-- practice band -->
    <rect class="practice-band" x="0" y="181" width="599" height="47" fill="var(--white)"/>
    <text class="practice-area" x="34" y="217" font-size="31" textLength="530" lengthAdjust="spacing">ACCIDENT &amp; INJURY LAW</text>

    <!-- firm name -->
    <circle cx="42" cy="291" r="13" fill="var(--red)"/>
    <text class="firm-name" x="64" y="298" font-size="21" textLength="178" lengthAdjust="spacing">HARLOW FIRM</text>

    <!-- divider -->
    <line x1="265" y1="248" x2="265" y2="340" stroke="var(--white)" stroke-width="1.5"/>

    <!-- phone -->
    <circle cx="295" cy="265" r="17" fill="var(--red)"/>
    <path d="M287 257 c2-2 4-2 5 0 l2 4 c1 2 0 3-1 4 l-1 1 c1 3 3 5 6 6 l1-1 c1-1 2-2 4-1 l4 2 c2 1 2 3 0 5 l-2 2 c-3 2-9 0-14-5 s-7-11-5-14z" fill="var(--white)"/>
    <text class="phone-number" x="320" y="285" font-size="48" textLength="252" lengthAdjust="spacingAndGlyphs">614.300.7000</text>

    <!-- disclaimer -->
    <text class="disclaimer" x="283" y="303" textLength="272" lengthAdjust="spacing">No Representation Made That The Quality</text>
    <text class="disclaimer" x="283" y="319">of Legal Services Performed is Greater</text>
    <text class="disclaimer" x="283" y="335">Than the Those of Other Attorneys</text>
  </svg>
</div>
</body>
</html>
```